Family owned plumbing contractor needs eye catching business card design

Business cards that are unique, eye catching, and provide customers with general company information, such as name, address, phone number, website, employee name/title, cell phone #, & email address. We are transitioning to a new logo that utilizes a more retro feel, so we are interested in seeing some cool old school designs in the mix. We are liking the dark background on some of the samples on this website. If that is workable with our artwork, we would like to see that incorporated into the design.
Contact Information for Business Card
Copperline Pipeworks, Inc.
www.copperlinepipeworks.example
(555) 392-7068 phone
Nevada License #64205
California License #5810473
Dale Wrennick, President
(555) 618-9032 cell
dale@copperlinepipeworks.example
Residential * Commercial * Service
Requirements
Must have
- The business card details listed above & logo provided.
Nice to have
- I made some notes about color options in the description.

```html
<!DOCTYPE html>
<html lang="en">
<head>
<meta charset="utf-8">
<title>Copperline Pipeworks, Inc. — Business Card</title>
<link rel="stylesheet" href="https://fonts.googleapis.com/css2?family=Lato:wght@400;700&display=swap">
<style>
  :root {
    --slate: #5a7d97;
    --teal: #7cc8bb;
    --white: #ffffff;
    --backdrop: #e9ecef;
    --ink-light: #f3f7fa;
  }
  * { box-sizing: border-box; margin: 0; padding: 0; }
  html, body { width: 1200px; height: 912px; overflow: hidden; }
  body {
    background: var(--backdrop);
    font-family: "Lato", sans-serif;
    display: flex;
    align-items: center;
    justify-content: center;
    gap: 48px;
  }
  .card {
    position: relative;
    width: 540px;
    height: 310px;
    border-radius: 18px;
    overflow: hidden;
    box-shadow: 0 6px 18px rgba(0,0,0,0.15);
  }
  /* Back */
  .card-back { background: var(--slate); }
  .card-back .brand {
    position: absolute;
    left: 50%; top: 42%;
    transform: translate(-50%, -50%);
    display: flex; align-items: center; gap: 12px;
    color: var(--white);
    font-weight: 700;
    font-size: 24px;
    white-space: nowrap;
  }
  .brand-dot {
    width: 18px; height: 18px; border-radius: 50%;
    background: var(--teal);
    flex: none;
  }
  .tagline {
    position: absolute;
    left: 0; right: 0; bottom: 46px;
    text-align: center;
    color: var(--ink-light);
    font-size: 16px;
    letter-spacing: 0.3px;
  }
  /* Front */
  .card-front { background: var(--white); }
  .card-front .wave { position: absolute; inset: 0; width: 100%; height: 100%; }
  .card-front .brand {
    position: absolute;
    left: 36px; top: 108px;
    display: flex; align-items: center; gap: 10px;
    color: var(--slate);
    font-weight: 700;
    font-size: 19px;
    white-space: nowrap;
  }
  .person {
    position: absolute;
    right: 30px; top: 20px;
    text-align: right;
  }
  .person-name {
    color: var(--slate);
    font-size: 22px;
    font-weight: 400;
    letter-spacing: 0.5px;
    text-transform: uppercase;
    line-height: 1.1;
  }
  .person-title { color: var(--teal); font-size: 13px; margin-top: 2px; }
  .details {
    position: absolute;
    right: 24px; top: 122px;
    text-align: right;
    color: var(--white);
    font-size: 12px;
    line-height: 1.45;
    list-style: none;
  }
  .details li { display: flex; justify-content: flex-end; align-items: center; gap: 7px; }
  .details .licences { margin-bottom: 8px; display: block; }
  .icon { width: 11px; height: 11px; flex: none; }
</style>
</head>
<body>

<section class="card card-back" aria-label="Card back">
  <div class="brand"><span class="brand-dot"></span>Copperline Pipeworks, Inc.</div>
  <p class="tagline">Residential * Commercial * Service</p>
</section>

<section class="card card-front" aria-label="Card front">
  <svg class="wave" viewBox="0 0 540 310" aria-hidden="true">
    <path class="wave-stripe" d="M110 222 C200 215 250 205 280 165 C320 110 380 78 540 70 L540 79 C400 88 340 115 302 170 C266 220 200 226 110 222 Z" fill="var(--slate)"/>
    <path class="wave-band" d="M0 228 C150 214 236 222 276 178 C246 230 150 238 0 244 Z" fill="var(--teal)"/>
    <path class="wave-body" d="M0 252 C160 240 250 246 292 182 C332 118 382 98 540 90 L540 310 L0 310 Z" fill="var(--slate)"/>
  </svg>

  <div class="brand"><span class="brand-dot"></span>Copperline Pipeworks, Inc.</div>

  <div class="person">
    <p class="person-name">Dale Wrennick</p>
    <p class="person-title">President</p>
  </div>

  <ul class="details">
    <li class="licences">Nevada License #64205<br>California License #5810473</li>
    <li>(555) 392-7068
      <svg class="icon" viewBox="0 0 24 24" aria-hidden="true"><path fill="currentColor" d="M6.6 10.8a15 15 0 0 0 6.6 6.6l2.2-2.2a1 1 0 0 1 1-.25 11.4 11.4 0 0 0 3.6.57 1 1 0 0 1 1 1V20a1 1 0 0 1-1 1A17 17 0 0 1 3 4a1 1 0 0 1 1-1h3.5a1 1 0 0 1 1 1c0 1.25.2 2.45.57 3.570a1 1 0 0 1-.25 1z"/></svg></li>
    <li>(555) 618-9032
      <svg class="icon" viewBox="0 0 24 24" aria-hidden="true"><rect x="6" y="2" width="12" height="20" rx="2" fill="none" stroke="currentColor" stroke-width="2"/><circle cx="12" cy="18" r="1.3" fill="currentColor"/></svg></li>
    <li>dale@copperlinepipeworks.example
      <svg class="icon" viewBox="0 0 24 24" aria-hidden="true"><rect x="2" y="5" width="20" height="14" rx="1" fill="none" stroke="currentColor" stroke-width="2"/><path d="M2 6l10 7 10-7" fill="none" stroke="currentColor" stroke-width="2"/></svg></li>
    <li>www.copperlinepipeworks.example
      <svg class="icon" viewBox="0 0 24 24" aria-hidden="true"><circle cx="12" cy="12" r="9" fill="none" stroke="currentColor" stroke-width="2"/><path d="M3 12h18M12 3c3 3 3 15 0 18M12 3c-3 3-3 15 0 18" fill="none" stroke="currentColor" stroke-width="1.6"/></svg></li>
  </ul>
</section>

</body>
</html>
```